I want a business letter head designed, one that I can have printed but also one that I can use as an insert for proforma documentation that is printed in house.

Business name : RJ Penfold & Associates
Address: PO Box 738
Tewantin Qld 4587

Type of business: Accounting practice- accounting, taxation, audit, self managed superannuation,

Colour scheme: black and blue - previously designed a business card; however the blue that is one the cards is very washed out and I am not particularly happy with it.

Industry/Entity Type

Business

```html
<!DOCTYPE html>
<html lang="en">
<head>
<meta charset="utf-8">
<title>RJ Penfold &amp; Associates — Letterhead</title>
<link rel="stylesheet" href="https://fonts.googleapis.com/css2?family=Arimo:wght@700&family=Open+Sans:wght@400&display=swap">
<style>
  :root {
    --brand-blue: #2794b9;
    --brand-black: #000000;
    --mark-charcoal: #1e1e1e;
    --paper: #ffffff;
    --address-aqua: #6fe3d8;
  }
  html, body {
    margin: 0;
    padding: 0;
    overflow: hidden;
    background: var(--paper);
  }
  .letterhead {
    position: relative;
    width: 925px;
    height: 1200px;
    overflow: hidden;
    background: var(--paper);
  }
  .letterhead__artwork {
    position: absolute;
    inset: 0;
    width: 925px;
    height: 1200px;
    display: block;
  }
  .artwork__blue { fill: var(--brand-blue); }
  .artwork__black { fill: var(--brand-black); }
  .artwork__paper { fill: var(--paper); }
  .artwork__square { fill: var(--brand-blue); }

  .business-name {
    position: absolute;
    left: 61px;
    top: 1044px;
    margin: 0;
    font-family: "Arimo", Arial, sans-serif;
    font-weight: 700;
    font-size: 27px;
    color: var(--mark-charcoal);
    letter-spacing: 0.2px;
  }
  .business-address {
    position: absolute;
    left: 77px;
    top: 1127px;
    margin: 0;
    font-family: "Open Sans", sans-serif;
    font-weight: 400;
    font-size: 20px;
    color: var(--address-aqua);
  }
  .brand-mark {
    position: absolute;
    right: 58px;
    top: 868px;
    display: flex;
    align-items: center;
    gap: 14px;
  }
  .brand-mark__square {
    width: 38px;
    height: 38px;
    background: var(--brand-blue);
  }
  .brand-mark__name {
    margin: 0;
    font-family: "Arimo", Arial, sans-serif;
    font-weight: 700;
    font-size: 46px;
    color: var(--mark-charcoal);
    line-height: 1;
  }
</style>
</head>
<body>
  <main class="letterhead">
    <svg class="letterhead__artwork" viewBox="0 0 694 900" preserveAspectRatio="none" aria-hidden="true">
      <!-- header band -->
      <rect class="artwork__blue" x="0" y="0" width="694" height="220"/>
      <path class="artwork__black" d="M250,103 L694,58 L694,220 Z"/>
      <!-- writing area -->
      <path class="artwork__paper" d="M0,150 C40,100 200,95 330,105 C480,118 600,160 694,195 L694,900 L0,900 Z"/>
      <!-- footer band -->
      <path class="artwork__blue" d="M0,705 C200,760 420,800 560,795 C620,790 660,775 694,760 L694,900 L0,900 Z"/>
      <path class="artwork__black" d="M0,840 L694,768 L694,900 L0,900 Z"/>
    </svg>

    <div class="brand-mark">
      <span class="brand-mark__square"></span>
      <p class="brand-mark__name">RJ Penfold</p>
    </div>

    <h1 class="business-name">RJ Penfold &amp; Associates</h1>
    <p class="business-address">Address: PO Box 738, Tewantin Qld 4587</p>
  </main>
</body>
</html>
```